Real estate Investment post card Design

I need a post card for Real Estate Marketing.

There are several similar cards on line.
Please see the post cards in this link to vidzorla
https://www.vidzorla.com/watch?v=pQmTr7W-b2Lx
At 1:18 the back of the card is very good.
For front of the card please refer to attached example gif.

Please also check the examples posted by me.

Everything needs to be the same except
1. Tomas Gets Homes
2. Phone number 287 914 5063
3. Website www.quillbrookestates.com
4. Email info@quillbrookestates.com
5. Picture needs to be replaced with my picture

The postcards need to be 2 sides and in color

Please let me know

Target Market(s)

Home owners who want to sell their houses for quick settlement and cash

Industry/Entity Type

Real Estate

Requirements
Must have
• I am copying this from another project as i think these instructions are valid for this project as well.
• Attention Designers - Special Requirements
• This project has special US Postcard Design requirements that apply to all submissions. The project is part of a print initiative, meaning that the selected design will be sent directly to print. If you have not, click download the templates below and ensure your design follows them before submitting.
• I plan to print the Post card by cardmillo in their Jumbo Format... copied below
• Document Trim Size
• 8.52" x 5.47"
• 216 x 139 mm
• 2556 x 1642 pixels
• Full Bleed Size
• Horizontal
• 8.64" x 5.59"
• 219 x 142 mm
• 2592 x 1677 pixels
• NOTE Please make sure you put return address on the post card
• 4725 7TH ST., PO Box. 5867
• BRIARWOOD FALLS, NY 11587
Nice to have
• Please see if you can add pictures that signify cash $$ and houses in the project. See the attached vidzorla.
Should not have
• Too much text on the first page

```html
<!DOCTYPE html>
<html lang="en">
<head>
<meta charset="utf-8">
<title>Tomas Gets Homes – Postcard</title>
<link href="https://fonts.googleapis.com/css2?family=Open+Sans:wdth,wght@75..100,400..800&family=Roboto+Condensed:ital,wght@0,400;0,700;1,400&family=Arimo:ital,wght@0,400;0,700;1,400;1,700&display=swap" rel="stylesheet">
<style>
  :root {
    --page: #ececec;
    --red: #d9131b;
    --red-dark: #a80d12;
    --navy: #0e2d52;
    --yellow: #ffc21a;
    --yellow-deep: #f5a300;
    --title-yellow: #ffd200;
    --panel: rgba(30, 30, 30, 0.88);
    --sky-top: #2f6ed0;
    --sky-bottom: #9cc4ee;
    --ink: #1b1b1b;
    --teal: #1fb6a6;
    --blue-text: #1d5a9c;
    --mail-grey: #e0ddd8;
    --white: #ffffff;
  }
  * { box-sizing: border-box; margin: 0; padding: 0; }
  html, body { width: 825px; height: 1200px; overflow: hidden; }
  body { background: var(--page); position: relative; font-family: "Arimo", Arial, sans-serif; }

  .card { position: absolute; left: 76px; width: 674px; overflow: hidden; box-shadow: 0 2px 6px rgba(0,0,0,0.25); }

  /* ---------- Front ---------- */
  .card--front { top: 113px; height: 435px; background: linear-gradient(180deg, var(--sky-top), var(--sky-bottom) 70%, #5d8a3a 88%, #4b7a2e); }
  .front__topband { position: absolute; left: 0; top: 0; width: 100%; height: 32px; background: linear-gradient(180deg, #e8262c, var(--red-dark)); }
  .front__house { position: absolute; left: 0; top: 32px; width: 100%; height: 403px;
    background: linear-gradient(180deg, rgba(255,255,255,0) 0%, rgba(214,214,210,0.9) 30%, #c9c9c4 70%, #6f8f46 92%); }
  .front__cash { position: absolute; left: 384px; top: 62px; width: 290px; height: 323px;
    background: linear-gradient(135deg, #eef0e8, #b9bdb0 60%, #d9b08c); border-radius: 6px; }
  .front__panel { position: absolute; left: 50px; top: 34px; width: 250px; height: 331px; background: var(--panel);
    font-family: "Open Sans", Arial, sans-serif; font-stretch: 82%; color: var(--white); }
  .front__name { position: absolute; left: 14px; top: 22px; font-size: 23px; font-weight: 700; white-space: nowrap; }
  .front__headline { position: absolute; left: 12px; top: 38px; font-size: 72px; font-weight: 800; line-height: 1; color: var(--yellow); white-space: nowrap; }
  .front__benefits { position: absolute; left: 22px; top: 138px; list-style: none; }
  .front__benefits li { display: flex; align-items: center; gap: 8px; font-size: 21px; font-weight: 700; height: 27px; white-space: nowrap; }
  .front__benefits svg { width: 16px; height: 16px; flex: none; }
  .front__promise { position: absolute; left: 19px; top: 252px; font-size: 14px; font-weight: 500; white-space: nowrap; }
  .front__phone { position: absolute; left: 42px; top: 307px; width: 269px; height: 58px; background: linear-gradient(180deg, #e8262c, var(--red-dark)); display: flex; align-items: center; gap: 14px; padding-left: 14px;
    font-family: "Open Sans", Arial, sans-serif; font-stretch: 80%; color: var(--white); font-size: 37px; font-weight: 700; white-space: nowrap; }
  .front__phone .icon { width: 30px; height: 30px; background: var(--white); border-radius: 4px; display: flex; align-items: center; justify-content: center; }
  .front__tagline { position: absolute; right: 0; bottom: 0; width: 362px; height: 50px; background: linear-gradient(180deg, #ffd437, var(--yellow-deep));
    clip-path: polygon(14px 0, 100% 0, 100% 100%, 0 100%); display: flex; align-items: center; justify-content: center; padding-left: 10px;
    font-family: "Open Sans", Arial, sans-serif; font-stretch: 78%; font-weight: 700; font-size: 16px; color: var(--red); white-space: nowrap; }

  /* ---------- Back ---------- */
  .card--back { top: 637px; height: 436px; background: var(--white); }
  .back__topband { position: absolute; left: 0; top: 0; width: 449px; height: 13px; background: var(--red); }
  .back__header { position: absolute; left: 0; top: 13px; width: 449px; height: 92px; background: var(--navy); }
  .back__title { position: absolute; left: 0; width: 100%; top: 11px; text-align: center; color: var(--title-yellow); font-weight: 700; font-size: 27px; white-space: nowrap; }
  .back__pill { position: absolute; left: 90px; top: 49px; width: 262px; height: 25px; border-radius: 5px; background: var(--white); text-align: center; font-style: italic; font-weight: 700; font-size: 16px; line-height: 25px; color: var(--ink); }
  .back__question { position: absolute; left: 20px; top: 112px; width: 420px; font-family: "Roboto Condensed", Arial, sans-serif; font-size: 20px; line-height: 25px; color: var(--ink); }
  .back__question em { color: var(--teal); }
  .back__rule { position: absolute; left: 19px; top: 166px; width: 428px; height: 1px; background: #333; }
  .back__reasons { position: absolute; top: 180px; list-style: none; font-size: 10px; line-height: 11.8px; color: var(--ink); }
  .back__reasons li::before { content: ""; display: inline-block; width: 4px; height: 4px; border-radius: 50%; background: #1d3fa8; margin-right: 4px; vertical-align: middle; }
  .back__reasons--a { left: 26px; } .back__reasons--b { left: 139px; } .back__reasons--c { left: 269px; }
  .back__portrait { position: absolute; left: 29px; top: 261px; width: 82px; height: 86px; background: linear-gradient(180deg, #f2f2f2, #9a9a9a 70%, #2b2b2b); }
  .back__contact { position: absolute; left: 143px; top: 255px; width: 188px; height: 93px; border-radius: 9px; background: var(--red); box-shadow: inset 0 0 0 2px rgba(255,255,255,0.35); padding: 12px 0 0 16px; color: var(--white); }
  .back__contact .name { font-size: 16px; font-weight: 700; line-height: 18px; }
  .back__contact .phone { font-size: 17px; font-weight: 700; color: #ffe14a; line-height: 19px; display: flex; align-items: center; gap: 6px; }
  .back__contact .line { font-size: 11px; line-height: 15px; display: flex; align-items: center; gap: 7px; }
  .back__contact svg { flex: none; }
  .back__cta { position: absolute; left: 32px; top: 364px; font-family: "Roboto Condensed", Arial, sans-serif; font-style: italic; font-size: 14.5px; color: var(--ink); white-space: nowrap; }
  .back__cta2 { position: absolute; left: 32px; top: 382px; font-family: "Roboto Condensed", Arial, sans-serif; font-size: 14.5px; color: var(--blue-text); white-space: nowrap; }
  .back__note { position: absolute; left: 32px; top: 404px; font-size: 8.5px; font-weight: 700; color: var(--ink); }
  .back__return { position: absolute; left: 470px; top: 38px; font-size: 9px; line-height: 11px; color: var(--ink); font-style: normal; }
  .back__stamp { position: absolute; left: 565px; top: 11px; width: 99px; height: 99px; background: var(--mail-grey); }
  .back__mailzone { position: absolute; left: 449px; top: 193px; width: 225px; height: 243px; background: var(--mail-grey); }
  .back__mailzone--low { left: 294px; top: 376px; width: 155px; height: 60px; }
</style>
</head>
<body>

<section class="card card--front" aria-label="Postcard front">
  <div class="front__topband"></div>
  <div class="front__house" role="img" aria-label="Photo of a two-storey white suburban house under a blue sky"></div>
  <div class="front__cash" role="img" aria-label="Photo of a hand holding a fan of hundred-dollar bills"></div>

  <div class="front__panel">
    <div class="front__name">TOMAS GETS HOMES</div>
    <div class="front__headline">CASH!</div>
    <ul class="front__benefits">
      <li><svg viewBox="0 0 16 16"><circle cx="8" cy="8" r="8" fill="#ffc21a"/><path d="M4.5 8.2l2.4 2.4 4.6-5" stroke="#1e1e1e" stroke-width="2" fill="none"/></svg>NO COMMISSIONS</li>
      <li><svg viewBox="0 0 16 16"><circle cx="8" cy="8" r="8" fill="#ffc21a"/><path d="M4.5 8.2l2.4 2.4 4.6-5" stroke="#1e1e1e" stroke-width="2" fill="none"/></svg>NO COSTS</li>
      <li><svg viewBox="0 0 16 16"><circle cx="8" cy="8" r="8" fill="#ffc21a"/><path d="M4.5 8.2l2.4 2.4 4.6-5" stroke="#1e1e1e" stroke-width="2" fill="none"/></svg>QUICK CASH</li>
      <li><svg viewBox="0 0 16 16"><circle cx="8" cy="8" r="8" fill="#ffc21a"/><path d="M4.5 8.2l2.4 2.4 4.6-5" stroke="#1e1e1e" stroke-width="2" fill="none"/></svg>SELL AS IS</li>
    </ul>
    <div class="front__promise">GET A CASH WITHIN 24 HOURS NOW!</div>
  </div>

  <div class="front__phone">
    <span class="icon"><svg width="18" height="18" viewBox="0 0 24 24"><path fill="#d9131b" d="M6.6 10.8a15.1 15.1 0 006.6 6.6l2.2-2.2c.3-.3.7-.4 1-.2 1.1.4 2.3.6 3.6.6.6 0 1 .4 1 1V20c0 .6-.4 1-1 1A17 17 0 013 4c0-.6.4-1 1-1h3.5c.6 0 1 .4 1 1 0 1.3.2 2.5.6 3.6.1.3 0 .7-.2 1z"/></svg></span>
    287 914 5063
  </div>

  <div class="front__tagline">ANY CONDITION.ANY SITUATION.ANY PROBLEM</div>
</section>

<section class="card card--back" aria-label="Postcard back">
  <div class="back__topband"></div>
  <div class="back__header">
    <div class="back__title">TOMAS GETS HOMES - CASH</div>
    <div class="back__pill">Any Condition! Any Situation</div>
  </div>

  <p class="back__question">Do you need to sell your property quickly for any of the following reasons?..<em>I Can Help!</em></p>
  <div class="back__rule"></div>

  <ul class="back__reasons back__reasons--a">
    <li>Inherited House</li><li>Debt Relief</li><li>Loss of Job</li><li>Forced Transfer</li><li>Failing Health</li>
  </ul>
  <ul class="back__reasons back__reasons--b">
    <li>Retirement</li><li>Tired Landlord</li><li>Out grown House</li><li>Little or No Equity</li><li>Bankruptcy</li>
  </ul>
  <ul class="back__reasons back__reasons--c">
    <li>Costly Repairs Needed</li><li>Can't Afford Payment</li><li>Moving to New House</li><li>Divorce</li><li>Foreclosure</li>
  </ul>

  <div class="back__portrait" role="img" aria-label="Portrait photo of the agent in a dark suit"></div>

  <div class="back__contact">
    <div class="name">Tomas Gets Homes</div>
    <div class="phone"><svg width="11" height="11" viewBox="0 0 24 24"><path fill="#fff" d="M6.6 10.8a15.1 15.1 0 006.6 6.6l2.2-2.2c.3-.3.7-.4 1-.2 1.1.4 2.3.6 3.6.6.6 0 1 .4 1 1V20c0 .6-.4 1-1 1A17 17 0 013 4c0-.6.4-1 1-1h3.5c.6 0 1 .4 1 1 0 1.3.2 2.5.6 3.6.1.3 0 .7-.2 1z"/></svg>287 914 5063</div>
    <div class="line"><svg width="10" height="10" viewBox="0 0 10 10"><circle cx="5" cy="5" r="4.3" fill="none" stroke="#fff"/><path d="M1 5h8M5 .7c-2 2.6-2 6 0 8.6M5 .7c2 2.6 2 6 0 8.6" stroke="#fff" fill="none" stroke-width=".8"/></svg>www.quillbrookestates.com</div>
    <div class="line"><svg width="10" height="8" viewBox="0 0 10 8"><rect x=".5" y=".5" width="9" height="7" fill="none" stroke="#fff"/><path d="M.5.5L5 4.5 9.5.5" stroke="#fff" fill="none"/></svg>info@quillbrookestates.com</div>
  </div>

  <p class="back__cta">Call today for FREE Private Consultation</p>
  <p class="back__cta2">Cash offer in 48 hours</p>
  <p class="back__note">Not ready to sell yet! Save this card</p>

  <address class="back__return">4725 7TH ST,<br>PO Box 5867,<br>BRIARWOOD FALLS,<br>NY 11587</address>
  <div class="back__stamp"></div>
  <div class="back__mailzone"></div>
  <div class="back__mailzone back__mailzone--low"></div>
</section>

</body>
</html>
```